Natural and organic skincare brand needs label design!

I need labels designed for my natural and organic skincare brand lumavale. The front of the bottles must contain the logo (image attached) and the following words: Formulated by a Naturopath; Anti-Aging Renewal; Organic Facial Oil; with CoEnzyme Q10 and Rosehip Seed Oil; 100ml e3.38fl.oz. Colours I would like used include black/white/grey/silver and aqua. I also like the grey woodgrain used on my draft website (check out www.lumavale-skin.com.au). The logo should be silver foil (shiny).The final design should be simple and communicate nature and sophistication. Some designs I like are found in the attachments. I intend to use black or white bottles.

Target Market(s)

women aged 30-50 interested in natural products

Industry/Entity Type

Skin Care Product

Font styles to use
Serif
Sans Serif
Decorative
Script
Other font styles liked:
• Any

Requirements
Must have
• Dimensions: 62mm (w) x 75mm (H) (front label only)
• Must contain the logo (image attached). The logo should be silver foil (shiny). and the following words are to be included on the label:
• Formulated by a Naturopath;
• Anti-Aging Renewal;
• Organic Facial Oil;
• with CoEnzyme Q10 and Rosehip Seed Oil;
• 100ml e3.38fl.oz.
Nice to have
• Colours I would like used include black/white/grey/silver and aqua (turquoise). But I am also open to suggestion. I also like the grey woodgrain used on my draft website (check out www.lumavale-skin.com.au)

```html
<!DOCTYPE html>
<html lang="en">
<head>
<meta charset="utf-8">
<title>lumavale — Anti-Aging Renewal Label</title>
<link href="https://fonts.googleapis.com/css2?family=Raleway:wght@300;400&display=swap" rel="stylesheet">
<style>
  :root {
    --paper: #ffffff;
    --slate: #4a5363;
    --ink: #4b4f58;
    --aqua: #3fd3d3;
    --wood-light: #f1f1f0;
    --wood-mid: #dcdcdb;
    --sketch: #e9eaec;
  }
  html, body {
    margin: 0;
    padding: 0;
    width: 991px;
    height: 1200px;
    overflow: hidden;
    background: var(--paper);
  }
  .label {
    position: relative;
    width: 991px;
    height: 1200px;
    background: var(--paper);
    font-family: "Raleway", sans-serif;
    color: var(--ink);
    text-align: center;
  }
  .label p, .label h1 { margin: 0; }
  .woodgrain-band {
    position: absolute;
    left: 0;
    top: 115px;
    width: 991px;
    height: 199px;
    background: linear-gradient(180deg, var(--wood-light) 0%, var(--wood-mid) 45%, var(--wood-light) 70%, var(--wood-mid) 100%);
  }
  .brand-badge {
    position: absolute;
    left: 364px;
    top: 16px;
    width: 243px;
    height: 243px;
    border-radius: 50%;
    background: var(--slate);
    border: 4px solid var(--paper);
    box-sizing: border-box;
    display: flex;
    align-items: center;
    justify-content: center;
  }
  .brand-name {
    font-weight: 300;
    font-size: 38px;
    letter-spacing: 3px;
    color: var(--paper);
  }
  .product-title {
    position: absolute;
    left: 0;
    width: 100%;
    font-weight: 300;
    color: var(--slate);
    line-height: 1;
    letter-spacing: 0;
    transform-origin: center;
  }
  .product-title--line1 { top: 402px; font-size: 104px; transform: scaleX(0.93); }
  .product-title--line2 { top: 500px; font-size: 136px; transform: scaleX(0.86); }
  .rule {
    position: absolute;
    left: 116px;
    width: 759px;
    height: 2px;
    background: var(--aqua);
  }
  .rule--upper { top: 658px; }
  .rule--lower { top: 1123px; }
  .product-type {
    position: absolute;
    top: 668px;
    left: 0;
    width: 100%;
    font-size: 52px;
    letter-spacing: 4px;
    color: var(--aqua);
    line-height: 1.1;
  }
  .product-ingredients {
    position: absolute;
    top: 728px;
    left: 0;
    width: 100%;
    font-size: 29px;
    color: var(--ink);
  }
  .botanical-art {
    position: absolute;
    left: 332px;
    top: 810px;
    width: 278px;
    height: 212px;
    border-radius: 40% 50% 45% 55%;
    background: radial-gradient(ellipse at center, var(--sketch) 0%, #f6f6f7 70%, var(--paper) 100%);
  }
  .formulator-note {
    position: absolute;
    top: 1055px;
    left: 0;
    width: 100%;
    font-size: 44px;
    color: var(--ink);
  }
  .volume {
    position: absolute;
    top: 1140px;
    left: 0;
    width: 100%;
    font-size: 34px;
    color: var(--ink);
  }
</style>
</head>
<body>
  <main class="label">
    <div class="woodgrain-band" role="img" aria-label="Grey whitewashed woodgrain texture band"></div>
    <div class="brand-badge">
      <span class="brand-name">lumavale</span>
    </div>

    <h1 class="product-title product-title--line1">ANTI-AGING</h1>
    <h1 class="product-title product-title--line2">RENEWAL</h1>

    <div class="rule rule--upper"></div>
    <p class="product-type">ORGANIC FACIAL OIL</p>
    <p class="product-ingredients">with CoEnzyme Q10 and Rosehip Seed Oil</p>

    <div class="botanical-art" role="img" aria-label="Fine line sketch of orchid flowers and leaves"></div>

    <p class="formulator-note">Formulated by a Naturopath</p>
    <div class="rule rule--lower"></div>
    <p class="volume">100ml&nbsp; e3.38fl.oz</p>
  </main>
</body>
</html>
```